Renewable Energy Consultancy needs relatively simple but smart website

We are a renewable energy focussed consultancy called Brenmoss, and we are just starting out. Our target is to bring knowledge of the detailed technical and commercial operations of renewables projects, mainly wind energy.

Our target customers are major energy utilities and private finance groups, who look to invest in renewables projects as a long term money-earning system. We are a fairly young, dynamic team of industry-respected people (4 of us) but we need to make ourselves look bigger than this (our customers will expect us to take on major projects, so we need to look big enough to handle it...)

We're not going to sell anything from our website and we expect it to just support our company name. Most of our customers are made by strong networks and relationships, so its mainly there to give confidence in our capabilities and give a strong view of who we are. We probably need a site with 4/5 pages which we can then expand when needed.

We have logos and headers (attached) which we want to use (also run through quillmarket), and I've attached a few pictures of projects similar to those we will be involved in to give us a feel for how it will look. Also attached are the colours we liked which are now used in the logo, and the font details. Whilst we're a "green" company with a "green" logo, we don't want to be completely green, so some nice combinations of colours on the pages would be good.

Ideally we need to have flenzo/torvaly news feeds somewhere linked into the site.

The design should be smart - giving a feel of high integrity and assurance whilst making us seem approachable and knowledgeable.

Target Market(s)

Renewables investors, developers of renewables projects (wind farms etc),

Industry/Entity Type

Finance

Coding

Coded - Design and coding required

Number of Pages Required

4 page

Other font styles liked:
• See the attachment with brand text/colour details ("colour codes" filename)

Requirements
Must have
• A fairly simple, but smart website design. We're looking to provide confidence and consolidate our networks with the website, not specifically find new customers - so its really just to give customers somewhere they can relate to online
Nice to have
• We have logos/brands and colours - so a website which incorperates these well and brings accross a professional company
• Would be nice to have a page (such as a blog/wordpress) we can easily update with news/events etc and links to flenzo feed and torvaly feed ideally.
Should not have
• cartoons, flashy gimmicks,

```html
<!DOCTYPE html>
<html lang="en">
<head>
<meta charset="utf-8">
<title>Brenmoss – Renewable Energy Consultancy</title>
<link href="https://fonts.googleapis.com/css2?family=Lato:wght@400;700;900&family=Signika:wght@400;600&family=Questrial&display=swap" rel="stylesheet">
<style>
:root{
  --green:#4f8a00;
  --green-bright:#6aab0c;
  --green-dark:#3d6e00;
  --footer:#568e00;
  --ink:#2a2a2a;
  --text:#444;
  --muted:#666;
  --nav:#2c2c2c;
  --white:#fff;
}
*{margin:0;padding:0;box-sizing:border-box}
html,body{width:1118px;height:1200px;overflow:hidden;background:var(--white)}
body{font-family:'Lato',sans-serif;color:var(--text)}
.page{position:relative;width:1118px;height:1200px;overflow:hidden}

/* header */
.site-header{position:absolute;left:0;top:0;width:1118px;height:103px;background:var(--white)}
.brand{position:absolute;left:103px;top:24px;display:flex;align-items:center;gap:14px}
.brand-dot{width:50px;height:50px;border-radius:50%;background:var(--green)}
.brand-name{font-family:'Lato',sans-serif;font-weight:400;font-size:46px;color:#555;letter-spacing:1px}
.follow{position:absolute;right:104px;top:39px;display:flex;align-items:center;gap:9px;font-size:17px;color:#333}
.follow .label{margin-right:6px}
.ring{width:26px;height:26px;border-radius:50%;border:2px solid #2e8ecf}

/* navigation */
.main-nav{position:absolute;left:0;top:103px;width:1118px;height:49px;background:var(--nav);border-bottom:3px solid var(--green-bright)}
.main-nav ul{list-style:none;position:absolute;left:106px;top:0;display:flex;height:46px;align-items:center}
.main-nav li{font-size:15px;color:#e6e6e6;padding:0 23px;border-left:1px solid #555;line-height:30px}
.main-nav li:first-child{border-left:0;color:var(--green-bright);position:relative}
.main-nav li:first-child::after{content:"";position:absolute;left:50%;bottom:-10px;margin-left:-5px;border:5px solid transparent;border-bottom-color:var(--green-bright)}
.nav-phone{position:absolute;right:103px;top:10px;display:flex;align-items:center;gap:10px;font-size:19px;color:var(--green-bright)}

/* hero */
.hero{position:absolute;left:0;top:152px;width:1118px;height:365px;
  background:linear-gradient(180deg,#3d7fc4 0%,#6ea5d9 35%,#b8d3ea 62%,#d9e6ef 74%,#5a8f2a 82%,#3f7a18 100%)}
.hero h1{position:absolute;left:110px;top:66px;font-weight:400;font-size:37px;line-height:36px;color:#1c1c1c}
.hero h1 strong{font-weight:900}
.hero p{position:absolute;left:111px;top:148px;width:450px;font-size:15px;line-height:21.5px;color:#3a3a3a}
.btn{position:absolute;left:111px;top:244px;width:128px;height:39px;border-radius:3px;background:linear-gradient(#5f9d0c,#3f7400);color:#fff;font-weight:700;font-size:16px;text-align:center;line-height:39px}

/* services band */
.services-band{position:absolute;left:0;top:517px;width:1118px;height:118px;background:linear-gradient(#3a3a3a,#151515)}
.service-card{position:absolute;top:17px;width:212px;height:79px;border-radius:40px 40px 0 40px;background:linear-gradient(#ffffff,#d8d8d8);display:flex;align-items:center}
.service-icon{width:75px;height:75px;margin-left:2px;border-radius:50%;background:radial-gradient(circle at 40% 35%,#74b51b,#3f7600);border:3px solid #e8e8e8;display:flex;align-items:center;justify-content:center}
.service-title{margin-left:11px;font-family:'Signika',sans-serif;font-size:18.5px;line-height:21px;color:#333;letter-spacing:.5px}
.service-title b{display:block;color:var(--green);font-weight:600}

/* content */
.column{position:absolute;top:660px}
.column h2{font-weight:700;font-size:22px;color:#555;padding-bottom:10px;border-bottom:1px solid #888}
.column p{margin-top:9px;padding-left:3px;width:276px;font-size:13px;line-height:21.3px;color:#444}
.more{position:absolute;top:864px;font-weight:700;font-size:15px;color:var(--green)}
.more span{margin-left:8px;font-size:12px}
.thumb{position:absolute;width:129px;height:65px;border:1px solid #ddd;padding:3px;background:#fff}
.thumb div{width:100%;height:100%}

/* footer */
.site-footer{position:absolute;left:0;top:905px;width:1118px;height:295px;background:var(--footer);color:#fff;font-family:'Questrial',sans-serif}
.site-footer h3{position:absolute;top:31px;font-weight:400;font-size:17.5px}
.site-footer ul{position:absolute;top:80px;list-style:none;font-size:13px;line-height:24.3px}
.contact-list{position:absolute;left:519px;top:79px;font-size:13px;line-height:20.5px}
.contact-row{display:flex;gap:10px;margin-bottom:10px}
.contact-row svg{flex:none;margin-top:2px}
.footer-brand{position:absolute;left:740px;top:97px;display:flex;align-items:center;gap:14px}
.footer-brand .brand-dot{width:46px;height:46px;background:#fff}
.footer-brand .brand-name{color:#fff;font-size:42px}
.footer-rule{position:absolute;left:117px;top:224px;width:883px;height:1px;background:rgba(255,255,255,.45)}
.copyright{position:absolute;left:116px;top:248px;font-size:13px}
.footer-social{position:absolute;left:857px;top:243px;display:flex;gap:11px}
.footer-social span{width:27px;height:27px;border-radius:50%;background:#fff}
</style>
</head>
<body>
<div class="page">

  <header class="site-header">
    <div class="brand"><span class="brand-dot"></span><span class="brand-name">Brenmoss</span></div>
    <div class="follow"><span class="label">Follow Us</span><span class="ring" aria-label="Social profile"></span><span class="ring" aria-label="flenzo profile"></span><span class="ring" aria-label="torvaly profile"></span></div>
  </header>

  <nav class="main-nav">
    <ul>
      <li>Home</li><li>Services</li><li>Wind Farms</li><li>Projects</li><li>About</li><li>Contact</li>
    </ul>
    <div class="nav-phone">
      <svg width="14" height="24" viewBox="0 0 14 24"><path d="M9 2 C3 4 2 20 9 22" fill="none" stroke="#fff" stroke-width="3" stroke-linecap="round"/></svg>
      1234 555 0187
    </div>
  </nav>

  <section class="hero" role="img" aria-label="Photograph of wind turbines on a green hillside under a blue sky">
    <h1>We are a <strong>renewable energy</strong><br>focussed consultancy</h1>
    <p>Lorem Ipsum is simply dummy text of the printing and typesetting industry. Lorem Ipsum has been the industry's standard dummy text ever since the 1500s, when an unknown printer took a galley of type and scrambled it to make a type specimen with book ending.</p>
    <div class="btn">Learn More</div>
  </section>

  <section class="services-band">
    <div class="service-card" style="left:105px">
      <div class="service-icon"><svg width="44" height="48" viewBox="0 0 44 48" fill="none" stroke="#fff" stroke-width="2.5" stroke-linecap="round"><path d="M22 18V46"/><path d="M22 18V2"/><path d="M22 18L6 28"/><path d="M22 18L38 28"/><circle cx="22" cy="18" r="2.5" fill="#fff"/></svg></div>
      <div class="service-title">BLADE AND<b>NACELLE</b></div>
    </div>
    <div class="service-card" style="left:335px">
      <div class="service-icon"><svg width="48" height="48" viewBox="0 0 48 48" fill="none" stroke="#fff" stroke-width="2.5"><circle cx="18" cy="28" r="14"/><path d="M4 28h28M18 14v28"/><circle cx="31" cy="16" r="9"/><path d="M37 22l8 8" stroke-width="4" stroke-linecap="round"/></svg></div>
      <div class="service-title">NEW SITE<b>COMMISION</b></div>
    </div>
    <div class="service-card" style="left:568px">
      <div class="service-icon"><svg width="44" height="40" viewBox="0 0 44 40" fill="none" stroke="#fff" stroke-width="2.5"><rect x="2" y="2" width="40" height="36"/><path d="M10 32v-8M17 32v-12M24 32v-6M31 32v-14" stroke-width="4"/><path d="M8 22L18 12l7 6 12-12"/></svg></div>
      <div class="service-title">RETURN TO<b>SERVICE</b></div>
    </div>
    <div class="service-card" style="left:798px">
      <div class="service-icon"><svg width="40" height="52" viewBox="0 0 40 52" fill="none" stroke="#fff" stroke-width="2.5"><path d="M20 4v10M12 20h16M10 50L16 20h8l6 30M14 32h12M12 42h16M14 32l12 10M26 32L14 42"/><circle cx="20" cy="10" r="4"/></svg></div>
      <div class="service-title">OIL ANALYSIS<b>FILTERATION</b></div>
    </div>
  </section>

  <section class="column" style="left:115px;width:257px">
    <h2>Welcome to Brenmoss</h2>
    <p>Lorem Ipsum is simply dummy text of the printing and typesetting industry. Lorem Ipsum has been the industry's standard dummy text ever since the 1500s, when an unknown printer took a galley of type and scrambled it to make a type specimen with book ending it to make a type specimen with book ending.</p>
  </section>
  <div class="more" style="left:118px">Read More<span>&gt;&gt;</span></div>

  <section class="column" style="left:425px;width:257px">
    <h2>From the Blog</h2>
    <p>Lorem Ipsum is simply dummy text of the printing and typesetting industry. Lorem Ipsum has been the industry's standard dummy text ever since the 1500s, when an unknown printer took a galley of type and scrambled it to make a type specimen with book ending it to make a type specimen with book ending.</p>
  </section>
  <div class="more" style="left:424px">Read More<span>&gt;&gt;</span></div>

  <section class="column" style="left:731px;width:267px">
    <h2>Our Projects</h2>
  </section>
  <div class="thumb" style="left:732px;top:714px"><div role="img" aria-label="Project photo of wind turbines in a field" style="background:linear-gradient(#5b98d6,#b9d4ea 70%,#6b7a3e)"></div></div>
  <div class="thumb" style="left:871px;top:714px"><div role="img" aria-label="Project photo of an engineer beside a turbine tower" style="background:linear-gradient(#1d4f9c,#6a9ad2 70%,#3e7d2c)"></div></div>
  <div class="thumb" style="left:732px;top:787px"><div role="img" aria-label="Project photo of wind turbines at sunset" style="background:linear-gradient(#3a2a6a,#e05a1a 55%,#f2b21e 75%,#2a1a10)"></div></div>
  <div class="thumb" style="left:871px;top:787px"><div role="img" aria-label="Project photo of a turbine installation vessel" style="background:linear-gradient(#c9d5e2,#8b9aa8 60%,#9a3a2a)"></div></div>
  <div class="more" style="left:732px">View All Projects<span>&gt;&gt;</span></div>

  <footer class="site-footer">
    <h3 style="left:117px">Sitemap</h3>
    <ul style="left:120px"><li>Home</li><li>Services</li><li>Wind Farms</li><li>About</li><li>Contact</li></ul>

    <h3 style="left:286px">Our Services</h3>
    <ul style="left:286px"><li>Lorem Ipsum Dolor Sit Amet</li><li>Typesetting Industry</li><li>Have been Sent in Lorem</li><li>Services Which Done</li><li>Inside Vehicula Quis</li></ul>

    <h3 style="left:523px">Contact Us</h3>
    <div class="contact-list">
      <div class="contact-row">
        <svg width="16" height="18" viewBox="0 0 16 18"><path d="M8 1a6 6 0 0 0-6 6c0 5 6 10 6 10s6-5 6-10a6 6 0 0 0-6-6z" fill="#fff"/><circle cx="8" cy="7" r="2.3" fill="#568e00"/></svg>
        <div>4820 Meadowline Road 19<br>Kestrel Vale, Dunmore<br>K4R 2P7</div>
      </div>
      <div class="contact-row">
        <svg width="16" height="14" viewBox="0 0 16 14"><rect x="1" y="2" width="14" height="10" fill="none" stroke="#fff" stroke-width="1.5"/><path d="M1 2l7 6 7-6" fill="none" stroke="#fff" stroke-width="1.5"/></svg>
        <div>loremipsum@mailpost.com</div>
      </div>
      <div class="contact-row">
        <svg width="16" height="16" viewBox="0 0 16 16"><path d="M4 1l3 4-2 2c1 2 2 3 4 4l2-2 4 3-2 3C7 15 1 9 1 3z" fill="#fff"/></svg>
        <div>888-555-0142</div>
      </div>
    </div>

    <div class="footer-brand"><span class="brand-dot"></span><span class="brand-name">Brenmoss</span></div>

    <div class="footer-rule"></div>
    <div class="copyright">© 2015 Brenmoss | Powered by Northgate Web Studio</div>
    <div class="footer-social"><span aria-label="flenzo profile"></span><span aria-label="Social profile"></span><span aria-label="Video channel"></span><span aria-label="News feed"></span></div>
  </footer>

</div>
</body>
</html>
```